Brightmoor Security Solutions window graphic

Looking for a graphic for my security company , Business for the back window of my truck. Make it look cool, please.

Call now for service (206) 555-0147
Brightmoorsecuritywa.example

“ Protection you can count on”

Target Market(s)

Auto security

Industry/Entity Type

Security

```html
<!DOCTYPE html>
<html lang="en">
<head>
<meta charset="utf-8">
<title>Brightmoor Security Solutions – Truck Window Graphic</title>
<link rel="stylesheet" href="https://fonts.googleapis.com/css2?family=Bebas+Neue&family=Michroma&family=Oswald:wght@500&display=swap">
<style>
  :root {
    --brand-orange: #ef4b24;
    --slate: #374652;
    --paper: #ffffff;
  }
  html, body {
    margin: 0;
    padding: 0;
    width: 1200px;
    height: 800px;
    overflow: hidden;
    background: var(--paper);
  }
  .window-graphic {
    display: block;
    width: 1200px;
    height: 800px;
  }
  .frame-outer { fill: none; stroke: var(--brand-orange); stroke-width: 20; }
  .frame-inner { fill: none; stroke: var(--slate); stroke-width: 20; }
  .stripe-orange, .rule, .call-band, .brand-dot { fill: var(--brand-orange); }
  .stripe-slate { fill: var(--slate); }
  .brand-name, .brand-sub {
    font-family: "Michroma", sans-serif;
    fill: var(--brand-orange);
  }
  .brand-name { font-size: 66px; }
  .brand-sub { font-size: 30px; }
  .tagline {
    font-family: "Michroma", sans-serif;
    font-size: 46px;
    fill: var(--slate);
  }
  .call-label {
    font-family: "Oswald", sans-serif;
    font-weight: 500;
    font-style: italic;
    font-size: 72px;
    fill: var(--paper);
  }
  .service-line {
    font-family: "Bebas Neue", sans-serif;
    font-size: 124px;
    fill: var(--slate);
  }
  .web-address {
    font-family: "Michroma", sans-serif;
    font-size: 44px;
    fill: var(--brand-orange);
  }
</style>
</head>
<body>
<svg class="window-graphic" viewBox="8 6 2334 1556" xmlns="http://www.w3.org/2000/svg">
  <!-- frames -->
  <rect class="frame-outer" x="501" y="329" width="1349" height="909"/>
  <rect class="frame-inner" x="542" y="369" width="1267" height="828"/>

  <!-- left speed stripes -->
  <polygon class="stripe-orange" points="735,421 771,421 657,770 621,770"/>
  <polygon class="stripe-slate" points="793,421 830,421 716,770 680,770"/>
  <polygon class="stripe-orange" points="851,421 889,421 775,770 739,770"/>

  <!-- right speed stripes -->
  <polygon class="stripe-orange" points="1463,421 1500,421 1613,770 1577,770"/>
  <polygon class="stripe-slate" points="1522,421 1558,421 1672,770 1636,770"/>
  <polygon class="stripe-orange" points="1580,421 1617,421 1731,770 1695,770"/>

  <!-- brand name -->
  <circle class="brand-dot" cx="1165" cy="545" r="95"/>
  <text class="brand-name" x="897" y="727" textLength="533" lengthAdjust="spacingAndGlyphs">BRIGHTMOOR</text>
  <text class="brand-sub" x="899" y="770" textLength="529" lengthAdjust="spacingAndGlyphs">SECURITY SOLUTIONS</text>

  <!-- tagline -->
  <text class="tagline" x="621" y="851" textLength="1110" lengthAdjust="spacingAndGlyphs">PROTECTION YOU CAN COUNT ON</text>

  <!-- call now band -->
  <rect class="rule" x="621" y="930" width="392" height="10"/>
  <rect class="rule" x="1311" y="930" width="420" height="10"/>
  <polygon class="call-band" points="1022,885 1325,886 1305,971 1003,970"/>
  <text class="call-label" x="1036" y="954" textLength="258" lengthAdjust="spacingAndGlyphs">CALL NOW</text>

  <!-- contact -->
  <text class="service-line" x="619" y="1086" textLength="1114" lengthAdjust="spacingAndGlyphs">FOR SERVICE (206) 555-0147</text>
  <text class="web-address" x="621" y="1146" textLength="1110" lengthAdjust="spacingAndGlyphs">BRIGHTMOORSECURITYWA.EXAMPLE</text>
</svg>
</body>
</html>
```